Money transfer app

I want a redesign of 3-4 screens of the mobile app.

I want:
1. Splash screen
2. Welcome screen
3. Login screen
4. More options. to send screen

I have attached existing designs.

```html
<!DOCTYPE html>
<html lang="en">
<head>
<meta charset="utf-8">
<title>Swiftsend – Money transfer app UX / UI Design</title>
<link rel="stylesheet" href="https://fonts.googleapis.com/css2?family=Inter:wght@300;400;500;600;700&family=Inter+Tight:wght@600;700;800&family=Noto+Serif:wght@400;500&display=swap">
<style>
  :root {
    --canvas: #647c5a;
    --forest: #053302;
    --forest-mid: #0f4a09;
    --lime: #86e35b;
    --btn-light: #4fae2e;
    --btn-dark: #0a3a06;
    --ink: #1b1b1b;
    --muted: #9a9a9a;
    --line: #cfcfcf;
    --card: #f1f1f1;
    --error: #e0413a;
    --link: #2c9fd6;
    --white: #ffffff;
  }
  * { margin: 0; padding: 0; box-sizing: border-box; }
  html, body { width: 942px; height: 1200px; overflow: hidden; }
  body {
    position: relative;
    background: var(--canvas);
    font-family: "Inter", sans-serif;
    color: var(--white);
  }
  .brand-tile {
    position: absolute; left: 80px; top: 73px;
    width: 89px; height: 89px; border-radius: 22px;
    background: var(--forest);
  }
  .deck-title {
    position: absolute; left: 184px; top: 76px;
    font-family: "Inter Tight", sans-serif; font-weight: 700;
    font-size: 37px; line-height: 43px; letter-spacing: -1.4px;
  }
  .section-title {
    position: absolute;
    font-family: "Inter Tight", sans-serif; font-weight: 700;
    font-size: 20px; letter-spacing: -0.5px;
  }
  .section-title--splash { left: 80px; top: 281px; }
  .section-title--onboarding { left: 483px; top: 281px; }
  .section-title--auth { left: 0; width: 946px; text-align: center; top: 621px; }
  .phone {
    position: absolute; width: 118px; height: 255px;
    border-radius: 17px; overflow: hidden; background: var(--white);
  }
  .phone svg { display: block; width: 118px; height: 255px; }
  .phone--splash { background: var(--forest); }
  .thanks {
    position: absolute; left: 480px; width: 400px; top: 985px;
    text-align: center;
    font-family: "Inter Tight", sans-serif; font-weight: 800;
    font-size: 76px; letter-spacing: -2.5px; line-height: 1;
  }
  .thanks-note {
    position: absolute; left: 480px; width: 400px; top: 1074px;
    text-align: center; font-weight: 300; font-size: 22px; line-height: 27px;
  }
  /* svg text */
  .ob-title { font-family: "Noto Serif", serif; font-size: 9.6px; fill: #2a2a2a; text-anchor: middle; }
  .ob-lead { font-family: "Noto Serif", serif; font-size: 7.6px; fill: #2a2a2a; text-anchor: middle; }
  .ob-small { font-size: 4.4px; fill: #6f6f6f; text-anchor: middle; }
  .card-label { font-size: 4.4px; font-weight: 700; fill: #1f1f1f; text-anchor: middle; }
  .card-desc { font-size: 3.2px; fill: #555; text-anchor: middle; }
  .btn-text { font-size: 5.8px; fill: var(--white); }
  .btn-text--dark { fill: var(--ink); }
  .auth-head { font-size: 6px; font-weight: 600; fill: var(--ink); }
  .field-label { font-size: 3.9px; fill: var(--muted); }
  .field-label--error { fill: var(--error); }
  .field-value { font-size: 4.2px; fill: var(--ink); }
  .field-error { font-size: 3.6px; fill: var(--error); }
  .link { font-size: 4.4px; fill: var(--link); }
  .app-name { font-size: 12px; font-weight: 600; fill: var(--white); text-anchor: middle; }
  .app-name--small { font-size: 7px; text-anchor: start; }
</style>
</head>
<body>

<svg width="0" height="0" style="position:absolute" aria-hidden="true">
  <defs>
    <linearGradient id="btn-fill" x1="0" x2="1" y1="0" y2="0">
      <stop offset="0" stop-color="var(--btn-light)"/>
      <stop offset="1" stop-color="var(--btn-dark)"/>
    </linearGradient>
    <linearGradient id="arc-fill" x1="0" x2="1" y1="0" y2="1">
      <stop offset="0" stop-color="#0b3d06"/>
      <stop offset="1" stop-color="#4fae2e"/>
    </linearGradient>
    <linearGradient id="art-fill" x1="0" x2="0" y1="0" y2="1">
      <stop offset="0" stop-color="#f7f7f7"/>
      <stop offset="1" stop-color="#e4e6e3"/>
    </linearGradient>
    <linearGradient id="spot-fill" x1="0" x2="1" y1="0" y2="1">
      <stop offset="0" stop-color="#cfe8b8"/>
      <stop offset="1" stop-color="#e8e8e8"/>
    </linearGradient>
    <symbol id="auth-header" viewBox="0 0 118 255">
      <ellipse cx="100" cy="-10" rx="80" ry="85" fill="var(--lime)"/>
      <ellipse cx="45" cy="5" rx="68" ry="90" fill="url(#arc-fill)"/>
      <ellipse cx="35" cy="-5" rx="60" ry="88" fill="var(--forest)"/>
      <text class="app-name app-name--small" x="14" y="37">swiftsend</text>
    </symbol>
    <symbol id="arrow" viewBox="0 0 6 6">
      <path d="M0.5 3H5.3M3.3 1L5.3 3L3.3 5" fill="none" stroke="currentColor" stroke-width="0.6"/>
    </symbol>
    <symbol id="eye" viewBox="0 0 6 4">
      <path d="M0.3 2C1.5 0.4 4.5 0.4 5.7 2C4.5 3.6 1.5 3.6 0.3 2Z" fill="#222"/>
      <circle cx="3" cy="2" r="0.8" fill="#fff"/>
    </symbol>
    <symbol id="tick" viewBox="0 0 6 5">
      <path d="M0.5 2.6L2.2 4.2L5.5 0.8" fill="none" stroke="var(--link)" stroke-width="0.6"/>
    </symbol>
  </defs>
</svg>

<div class="brand-tile" aria-hidden="true"></div>
<h1 class="deck-title">Swiftsend - Money transfer app :<br>UX / UI Design</h1>

<h2 class="section-title section-title--splash">Splash screen</h2>
<h2 class="section-title section-title--onboarding">Onboarding screen</h2>

<!-- Splash -->
<div class="phone phone--splash" style="left:84px;top:322px">
  <svg viewBox="0 0 118 255">
    <text class="app-name" x="59" y="126">swiftsend</text>
    <rect x="38" y="248" width="40" height="1.6" rx="0.8" fill="#fff"/>
  </svg>
</div>

<!-- Onboarding: welcome -->
<div class="phone" style="left:309px;top:322px">
  <svg viewBox="0 0 118 255">
    <text class="ob-title" x="59" y="30">Welcome to Swift</text>
    <text class="ob-title" x="59" y="42">Send</text>
    <rect x="0" y="52" width="118" height="120" fill="url(#art-fill)" role="img" aria-label="Line illustration of a harbour city skyline with clouds"/>
    <text class="ob-lead" x="59" y="189">Sending money made</text>
    <text class="ob-lead" x="59" y="199">Simple, Fast &amp; Transparent</text>
    <text class="ob-small" x="59" y="210">Send money online 24/7 when it's</text>
    <text class="ob-small" x="59" y="217">convenient for you</text>
    <rect x="7" y="226" width="102" height="15" rx="7.5" fill="url(#btn-fill)"/>
    <text class="btn-text" x="14" y="235.5">Next</text>
    <use href="#arrow" x="97" y="230.5" width="6" height="6" color="#fff"/>
    <rect x="38" y="248" width="40" height="1.6" rx="0.8" fill="#111"/>
  </svg>
</div>

<!-- Onboarding: why choose -->
<div class="phone" style="left:442px;top:322px">
  <svg viewBox="0 0 118 255">
    <text class="ob-title" x="59" y="33">Why Choose Swift</text>
    <text class="ob-title" x="59" y="45">Send</text>
    <rect x="0" y="120" width="118" height="98" fill="url(#art-fill)" role="img" aria-label="Faint line illustration of a city skyline"/>
    <rect x="8" y="72" width="50" height="50" rx="4" fill="var(--card)"/>
    <rect x="12" y="62" width="40" height="34" rx="3" fill="url(#spot-fill)" role="img" aria-label="Illustration of coins exchanging currencies"/>
    <text class="card-label" x="33" y="103">SIMPLE</text>
    <text class="card-desc" x="33" y="109">Easy to use and available</text>
    <text class="card-desc" x="33" y="113">around the clock</text>
    <rect x="61" y="72" width="50" height="50" rx="4" fill="var(--card)"/>
    <rect x="65" y="64" width="44" height="32" rx="3" fill="url(#spot-fill)" role="img" aria-label="Illustration of a flying banknote"/>
    <text class="card-label" x="86" y="103" style="font-weight:500">FAST</text>
    <text class="card-desc" x="86" y="109">Money send will be</text>
    <text class="card-desc" x="86" y="113">available in minute</text>
    <rect x="8" y="127" width="50" height="55" rx="4" fill="var(--card)"/>
    <rect x="12" y="130" width="42" height="28" rx="3" fill="url(#spot-fill)" role="img" aria-label="Illustration of two phones exchanging money"/>
    <text class="card-label" x="33" y="167" style="font-weight:500">TRANSPARENT</text>
    <text class="card-desc" x="33" y="173">Our low fees exchange</text>
    <text class="card-desc" x="33" y="177">ratesare shown from start</text>
    <rect x="7" y="224" width="102" height="15" rx="7.5" fill="url(#btn-fill)"/>
    <text class="btn-text" x="14" y="233.5">Next</text>
    <use href="#arrow" x="97" y="228.5" width="6" height="6" color="#fff"/>
    <rect x="38" y="248" width="40" height="1.6" rx="0.8" fill="#111"/>
  </svg>
</div>

<!-- Onboarding: how it works -->
<div class="phone" style="left:575px;top:322px">
  <svg viewBox="0 0 118 255">
    <text class="ob-title" x="59" y="33">How it Works</text>
    <rect x="0" y="120" width="118" height="98" fill="url(#art-fill)" role="img" aria-label="Faint line illustration of a city skyline"/>
    <rect x="7" y="60" width="48" height="50" rx="4" fill="var(--card)"/>
    <rect x="10" y="54" width="40" height="38" rx="3" fill="url(#spot-fill)" role="img" aria-label="Illustration of choosing a country on a map"/>
    <text class="card-label" x="31" y="101" style="font-weight:600">Select Country</text>
    <rect x="60" y="60" width="49" height="50" rx="4" fill="var(--card)"/>
    <rect x="64" y="54" width="40" height="38" rx="3" fill="url(#spot-fill)" role="img" aria-label="Illustration of picking a product on a phone"/>
    <text class="card-label" x="84.5" y="101" style="font-weight:600">Select Product</text>
    <rect x="7" y="117" width="48" height="53" rx="4" fill="var(--card)"/>
    <rect x="10" y="113" width="40" height="40" rx="3" fill="url(#spot-fill)" role="img" aria-label="Illustration of adding a recipient on a clipboard"/>
    <text class="card-label" x="31" y="164" style="font-weight:600">Add Recipient</text>
    <rect x="60" y="117" width="49" height="53" rx="4" fill="var(--card)"/>
    <rect x="64" y="116" width="40" height="37" rx="3" fill="url(#spot-fill)" role="img" aria-label="Illustration of confirming a payment on a phone"/>
    <text class="card-label" x="84.5" y="164" style="font-weight:600">Confirm &amp; Pay</text>
    <rect x="7" y="224" width="102" height="15" rx="7.5" fill="url(#btn-fill)"/>
    <text class="btn-text" x="14" y="233.5">Next</text>
    <use href="#arrow" x="97" y="228.5" width="6" height="6" color="#fff"/>
    <rect x="38" y="248" width="40" height="1.6" rx="0.8" fill="#111"/>
  </svg>
</div>

<!-- Onboarding: more options -->
<div class="phone" style="left:708px;top:322px">
  <svg viewBox="0 0 118 255">
    <text class="ob-title" x="59" y="33">More Option To Send</text>
    <rect x="0" y="120" width="118" height="98" fill="url(#art-fill)" role="img" aria-label="Faint line illustration of a city skyline"/>
    <rect x="8" y="58" width="49" height="51" rx="4" fill="var(--card)"/>
    <rect x="11" y="50" width="42" height="33" rx="3" fill="url(#spot-fill)" role="img" aria-label="Illustration of a phone used as a mobile wallet"/>
    <text class="card-label" x="32.5" y="90">MOBILE MONEY</text>
    <text class="card-desc" x="32.5" y="96">Realtime transfer to</text>
    <text class="card-desc" x="32.5" y="100">mobile wallet</text>
    <rect x="61" y="58" width="49" height="51" rx="4" fill="var(--card)"/>
    <rect x="64" y="50" width="42" height="33" rx="3" fill="url(#spot-fill)" role="img" aria-label="Illustration of a cash pickup card"/>
    <text class="card-label" x="85.5" y="90">CASH PICKUP</text>
    <text class="card-desc" x="85.5" y="96">Pickup from our large</text>
    <text class="card-desc" x="85.5" y="100">network of agents</text>
    <rect x="8" y="119" width="49" height="49" rx="4" fill="var(--card)"/>
    <rect x="11" y="116" width="42" height="26" rx="3" fill="url(#spot-fill)" role="img" aria-label="Illustration of a bank building with coins"/>
    <text class="card-label" x="32.5" y="149">BANK DEPOSIT</text>
    <text class="card-desc" x="32.5" y="155">Instant transfer to</text>
    <text class="card-desc" x="32.5" y="159">Bank Account</text>
    <rect x="7" y="224" width="102" height="15" rx="7.5" fill="url(#btn-fill)"/>
    <text class="btn-text" x="14" y="233.5">Next</text>
    <use href="#arrow" x="97" y="228.5" width="6" height="6" color="#fff"/>
    <rect x="38" y="248" width="40" height="1.6" rx="0.8" fill="#111"/>
  </svg>
</div>

<h2 class="section-title section-title--auth">Sign in / Sign up screen</h2>

<!-- Auth: landing -->
<div class="phone" style="left:80px;top:662px">
  <svg viewBox="0 0 118 255">
    <rect x="0" y="126" width="118" height="60" fill="url(#art-fill)" role="img" aria-label="Line illustration of a harbour city skyline"/>
    <ellipse cx="110" cy="30" rx="95" ry="98" fill="var(--lime)"/>
    <ellipse cx="60" cy="10" rx="100" ry="118" fill="url(#arc-fill)"/>
    <ellipse cx="30" cy="0" rx="80" ry="105" fill="var(--forest)"/>
    <text class="app-name app-name--small" x="14" y="45">swiftsend</text>
    <rect x="9" y="195" width="100" height="15" rx="7.5" fill="url(#btn-fill)"/>
    <text class="btn-text" x="17" y="204.5">Sign in</text>
    <use href="#arrow" x="97" y="199.5" width="6" height="6" color="#fff"/>
    <rect x="9.3" y="215.3" width="99.4" height="14.4" rx="7.2" fill="#fff" stroke="#3d8a24" stroke-width="0.6"/>
    <text class="btn-text btn-text--dark" x="17" y="224.5">Sign up</text>
    <use href="#arrow" x="97" y="219.5" width="6" height="6" color="#333"/>
    <rect x="38" y="248" width="40" height="1.6" rx="0.8" fill="#111"/>
  </svg>
</div>

<!-- Auth: sign in -->
<div class="phone" style="left:213px;top:662px">
  <svg viewBox="0 0 118 255">
    <use href="#auth-header" width="118" height="255"/>
    <text class="auth-head" x="9" y="109">Sign in</text>
    <text class="field-label" x="9" y="128">Email Address</text>
    <text class="field-value" x="9" y="135.5">lena.marsh@mail.com</text>
    <use href="#tick" x="100" y="130" width="6" height="5"/>
    <line x1="9" x2="109" y1="138.5" y2="138.5" stroke="var(--line)" stroke-width="0.4"/>
    <text class="field-label" x="9" y="150.5">Password</text>
    <text class="field-value" x="9" y="158">··············</text>
    <use href="#eye" x="99" y="154.5" width="5" height="3.5"/>
    <line x1="9" x2="109" y1="161" y2="161" stroke="var(--line)" stroke-width="0.4"/>
    <text class="link" x="9" y="172.5">Forgot Password?</text>
    <rect x="9" y="215" width="100" height="15" rx="7.5" fill="url(#btn-fill)"/>
    <text class="btn-text" x="17" y="224.5">Sign in</text>
    <use href="#arrow" x="97" y="219.5" width="6" height="6" color="#fff"/>
    <rect x="38" y="248" width="40" height="1.6" rx="0.8" fill="#111"/>
  </svg>
</div>

<!-- Auth: sign up -->
<div class="phone" style="left:346px;top:662px">
  <svg viewBox="0 0 118 255">
    <use href="#auth-header" width="118" height="255"/>
    <text class="auth-head" x="9" y="109">Sign up</text>
    <text class="field-label" x="9" y="128">Email Address</text>
    <text class="field-value" x="9" y="138">lena.marsh@mail.com</text>
    <use href="#tick" x="100" y="133" width="6" height="5"/>
    <line x1="9" x2="109" y1="141" y2="141" stroke="var(--line)" stroke-width="0.4"/>
    <text class="field-label" x="9" y="152.5">Password</text>
    <text class="field-value" x="9" y="161">·············</text>
    <use href="#eye" x="99" y="158" width="5" height="3.5"/>
    <line x1="9" x2="109" y1="164.5" y2="164.5" stroke="var(--line)" stroke-width="0.4"/>
    <text class="field-label" x="9" y="177">Repeat Password</text>
    <text class="field-value" x="9" y="185">·············</text>
    <use href="#eye" x="99" y="182" width="5" height="3.5"/>
    <line x1="9" x2="109" y1="188.5" y2="188.5" stroke="var(--line)" stroke-width="0.4"/>
    <rect x="9" y="215" width="100" height="15" rx="7.5" fill="url(#btn-fill)"/>
    <text class="btn-text" x="17" y="224.5">Sign up</text>
    <use href="#arrow" x="97" y="219.5" width="6" height="6" color="#fff"/>
    <rect x="38" y="248" width="40" height="1.6" rx="0.8" fill="#111"/>
  </svg>
</div>

<!-- Auth: sign up, email error -->
<div class="phone" style="left:479px;top:662px">
  <svg viewBox="0 0 118 255">
    <use href="#auth-header" width="118" height="255"/>
    <text class="auth-head" x="9" y="109">Sign up</text>
    <text class="field-label field-label--error" x="9" y="128">Email Address</text>
    <text class="field-value" x="9" y="138">lena.marsh@mail</text>
    <line x1="9" x2="109" y1="141" y2="141" stroke="var(--line)" stroke-width="0.4"/>
    <text class="field-error" x="9" y="147">The email address is wrong.</text>
    <text class="field-label" x="9" y="158.5">Password</text>
    <text class="field-value" x="9" y="167">·············</text>
    <use href="#eye" x="99" y="164" width="5" height="3.5"/>
    <line x1="9" x2="109" y1="170.5" y2="170.5" stroke="var(--line)" stroke-width="0.4"/>
    <text class="field-label" x="9" y="183">Repeat Password</text>
    <text class="field-value" x="9" y="191">·············</text>
    <use href="#eye" x="99" y="188.5" width="5" height="3.5"/>
    <line x1="9" x2="109" y1="194.5" y2="194.5" stroke="var(--line)" stroke-width="0.4"/>
    <rect x="9" y="215" width="100" height="15" rx="7.5" fill="url(#btn-fill)"/>
    <text class="btn-text" x="17" y="224.5">Sign up</text>
    <use href="#arrow" x="97" y="219.5" width="6" height="6" color="#fff"/>
    <rect x="38" y="248" width="40" height="1.6" rx="0.8" fill="#111"/>
  </svg>
</div>

<!-- Auth: sign up, password error -->
<div class="phone" style="left:612px;top:662px">
  <svg viewBox="0 0 118 255">
    <use href="#auth-header" width="118" height="255"/>
    <text class="auth-head" x="9" y="109">Sign up</text>
    <text class="field-label" x="9" y="123">Email Address</text>
    <text class="field-value" x="9" y="133">lena.marsh@mail.com</text>
    <line x1="9" x2="109" y1="136" y2="136" stroke="var(--link)" stroke-width="0.4"/>
    <text class="field-label field-label--error" x="9" y="147">Password</text>
    <text class="field-value" x="9" y="156">·············</text>
    <use href="#eye" x="99" y="153" width="5" height="3.5"/>
    <line x1="9" x2="109" y1="159.5" y2="159.5" stroke="var(--line)" stroke-width="0.4"/>
    <text class="field-error" x="9" y="167">The passwords doesn't match.</text>
    <text class="field-label" x="9" y="176">Repeat Password</text>
    <text class="field-value" x="9" y="184.5">·············</text>
    <use href="#eye" x="99" y="181.5" width="5" height="3.5"/>
    <line x1="9" x2="109" y1="188" y2="188" stroke="var(--line)" stroke-width="0.4"/>
    <rect x="9" y="215" width="100" height="15" rx="7.5" fill="url(#btn-fill)"/>
    <text class="btn-text" x="17" y="224.5">Sign up</text>
    <use href="#arrow" x="97" y="219.5" width="6" height="6" color="#fff"/>
    <rect x="38" y="248" width="40" height="1.6" rx="0.8" fill="#111"/>
  </svg>
</div>

<!-- Auth: forgotten password -->
<div class="phone" style="left:745px;top:662px">
  <svg viewBox="0 0 118 255">
    <use href="#auth-header" width="118" height="255"/>
    <text class="auth-head" x="9" y="109">Forgotten Password</text>
    <text class="field-label" x="9" y="134">Email Address</text>
    <text class="field-value" x="9" y="144.5">lena.marsh@mail.com</text>
    <use href="#tick" x="100" y="139" width="6" height="5"/>
    <line x1="9" x2="109" y1="147.5" y2="147.5" stroke="var(--link)" stroke-width="0.4"/>
    <text class="field-error" x="9" y="153.5">Please Enter Your Registered Email</text>
    <rect x="9" y="215" width="100" height="15" rx="7.5" fill="url(#btn-fill)"/>
    <text class="btn-text" x="17" y="224.5">Reset Password</text>
    <use href="#arrow" x="97" y="219.5" width="6" height="6" color="#fff"/>
    <rect x="38" y="248" width="40" height="1.6" rx="0.8" fill="#111"/>
  </svg>
</div>

<p class="thanks">Thank you</p>
<p class="thanks-note">Your feedback matters to us. Let us know what you think!</p>

</body>
</html>
```